Sidewalk Sign For Laundry Service

I'd like to make a sign that offers *free* laundry service for the next customers that bring in their laundry. There needs to be some immediacy in the design. The idea is to put out this sign when we are idle in the laundry and want to use the time to attract new customers. So somehow we need to communicate that the offer is for right now and will likely be gone in an hour or two. Attached are photos of the sign holder in place to give a feel for the location and environment. Obviously I'm looking for a much better design that the one currently in use.

Requirements:
* 23.25" x 35.5" - the full width will be visible but the top and bottom 0.5" will be hidden by the sign holder. It will be printed on coroplast.
* Must include a large arrow to show where the service is offered. We're off the main street so the arrow helps a lot. See the attached pictures of the sign being replaced.
* Needs to be visible to cars as they drive by.
* For the final product I'll need three versions. One with an arrow pointing to the right, one with an arrow pointing to the left, and one to go in the store window with no arrow.

Background on the service: We sort, wash, dry, and fold the laundry for customers and then neatly put it in a nice laundry bag that makes returning very convenient. Their laundry comes out fresh, clean, smelling great, and without the hassle of doing it themselves. We have a great return rate. Most customers that try out the service become long term customers.

Attached are two pictures of the sign holder with our current "Laundry Wash & Fold" sign. Also, our logo which would be nice to include to help with branding.

```html
<!DOCTYPE html>
<html lang="en">
<head>
<meta charset="utf-8">
<title>Wash &amp; Fold Sidewalk Sign Options</title>
<link rel="stylesheet" href="https://fonts.googleapis.com/css2?family=Montserrat:wght@400;800;900&display=swap">
<style>
  :root {
    --canvas: #ffffff;
    --frame: #808080;
    --navy: #233f94;
    --orange: #f26522;
    --peach: #f9b48c;
    --sky: #8ebde6;
    --sky-pale: #e4f0fb;
    --sky-text: #b9d8f3;
    --night: #1f201c;
    --white: #ffffff;
  }
  * { box-sizing: border-box; margin: 0; padding: 0; }
  html, body { width: 1200px; height: 712px; overflow: hidden; background: var(--canvas); }
  body { position: relative; font-family: "Montserrat", Arial, sans-serif; }

  .choice-word {
    position: absolute; left: 378px; top: 40px;
    font-weight: 400; font-size: 72px; line-height: 1; color: #000;
  }

  .sign {
    position: absolute; width: 335px; height: 504px;
    border: 11px solid var(--frame); background: var(--white);
    overflow: hidden;
  }
  .sign--blue { left: 76px; top: 141px; }
  .sign--orange { left: 432px; top: 141px; }

  .brand {
    position: absolute; left: 0; top: 0; width: 100%; height: 133px;
    display: flex; align-items: center; gap: 12px; padding-left: 16px;
  }
  .brand-square { width: 66px; height: 66px; background: var(--navy); flex: none; }
  .brand-name { font-weight: 800; font-size: 30px; color: var(--navy); letter-spacing: 0.3px; white-space: nowrap; }

  .stripe { position: absolute; left: 0; width: 100%; height: 13px; }
  .stripe--upper { top: 133px; }
  .stripe--lower { top: 287px; }
  .sign--blue .stripe { background: var(--orange); }
  .sign--orange .stripe { background: var(--navy); }

  .headline {
    position: absolute; left: 0; top: 146px; width: 100%; height: 141px;
    display: flex; flex-direction: column; align-items: center; justify-content: center;
    text-transform: uppercase; font-weight: 900; line-height: 1;
  }
  .sign--blue .headline { background: linear-gradient(#ffffff, var(--sky-pale) 40%, var(--sky)); }
  .sign--orange .headline { background: linear-gradient(#ffffff, #fde3d2 45%, var(--peach)); }
  .headline-main { font-size: 46px; letter-spacing: 1px; }
  .headline-sub { font-size: 31px; color: var(--navy); margin-top: 4px; letter-spacing: 0.5px; }
  .sign--blue .headline-main { color: var(--orange); }
  .sign--orange .headline-main { color: var(--navy); }

  .offer { position: absolute; left: 0; top: 300px; width: 100%; height: 182px; }
  .sign--blue .offer { background: var(--sky); }
  .sign--orange .offer { background: var(--orange); }
  .offer-arrow { position: absolute; left: 12px; top: 34px; width: 293px; height: 115px; }
  .offer-text { font-family: "Montserrat", Arial, sans-serif; font-weight: 900; font-size: 40px; }

  .night-panel {
    position: absolute; left: 794px; top: 138px; width: 370px; height: 507px;
    background: var(--night);
  }
  .night-panel .sign {
    left: 71px; top: 111px; width: 313px; height: 482px; border: 0;
    transform: scale(0.69); transform-origin: top left;
  }
</style>
</head>
<body>
  <div class="choice-word">or</div>

  <section class="sign sign--blue" aria-label="Sign option in blue">
    <header class="brand"><span class="brand-square"></span><span class="brand-name">Suds on Elm</span></header>
    <div class="stripe stripe--upper"></div>
    <div class="headline"><span class="headline-main">Laundry</span><span class="headline-sub">Wash&amp;Fold</span></div>
    <div class="stripe stripe--lower"></div>
    <div class="offer">
      <svg class="offer-arrow" viewBox="0 0 293 115" aria-label="Arrow pointing right">
        <polygon points="0,29 205,29 205,0 293,57 205,115 205,86 0,86" fill="var(--navy)"/>
        <text class="offer-text" x="12" y="72" textLength="200" lengthAdjust="spacingAndGlyphs" fill="var(--sky-text)">FREE NOW</text>
      </svg>
    </div>
  </section>

  <section class="sign sign--orange" aria-label="Sign option in orange">
    <header class="brand"><span class="brand-square"></span><span class="brand-name">Suds on Elm</span></header>
    <div class="stripe stripe--upper"></div>
    <div class="headline"><span class="headline-main">Laundry</span><span class="headline-sub">Wash&amp;Fold</span></div>
    <div class="stripe stripe--lower"></div>
    <div class="offer">
      <svg class="offer-arrow" viewBox="0 0 293 115" aria-label="Arrow pointing right">
        <polygon points="0,29 205,29 205,0 293,57 205,115 205,86 0,86" fill="var(--white)"/>
        <text class="offer-text" x="12" y="72" textLength="200" lengthAdjust="spacingAndGlyphs" fill="var(--orange)">FREE NOW</text>
      </svg>
    </div>
  </section>

  <div class="night-panel" role="img" aria-label="Night street scene with the orange sign standing in its holder">
    <section class="sign sign--orange">
      <header class="brand"><span class="brand-square"></span><span class="brand-name">Suds on Elm</span></header>
      <div class="stripe stripe--upper"></div>
      <div class="headline"><span class="headline-main">Laundry</span><span class="headline-sub">Wash&amp;Fold</span></div>
      <div class="stripe stripe--lower"></div>
      <div class="offer">
        <svg class="offer-arrow" viewBox="0 0 293 115" aria-label="Arrow pointing right">
          <polygon points="0,29 205,29 205,0 293,57 205,115 205,86 0,86" fill="var(--white)"/>
          <text class="offer-text" x="12" y="72" textLength="200" lengthAdjust="spacingAndGlyphs" fill="var(--orange)">FREE NOW</text>
        </svg>
      </div>
    </section>
  </div>
</body>
</html>
```